New York City Sponsorship Page with Click Through Supporting Pages

Metro Talent Guild, the leading New York City resource for HR Professionals is a membership organization with almost 2,000 individual members.

We need section/page(s) created for our current sponsorship offerings. Our platform is on ClubNest Suite Platform and we need capability to edit the page, etc. It must be HTML ready/coded.

Attached is the mock up of how we want the page to look (pages mockup pdf) as well as each of the categories which should be included (in the excel files). Our current page is here: http://www.metrotalentguild.example/?page=sponsors and is not easy to read through. We want something that is visually appealing and clean but showcases all of the different ways to sponsor the Chapter.

Additionally, we are taking the information from this page and turning it into a brochure.

Target Market(s)

New York City Companies who have HR Professionals or services they want to attract or offer.

Coding

Coded - Design and coding required

Number of Pages Required

5+ page

Requirements
Must have
• Clean Look and feel, easy functionality, necessary information and purchases. Match the top navigation of current page. Opportunity for current sponsor logos to be highlighted on the page. Easy to update/maintain.
Nice to have
• Option to pay for sponsorships through the page using our credit card processor.
Should not have
• Overwhelming text in sections

```html
<!DOCTYPE html>
<html lang="en">
<head>
<meta charset="utf-8">
<title>Invitation for Sponsors – Metro Talent Guild</title>
<link href="https://fonts.googleapis.com/css2?family=Anton&family=Open+Sans:wght@400;600;700&display=swap" rel="stylesheet">
<style>
:root{
  --topbar:#3a3a3a;
  --nav-blue:#1a8fd0;
  --brand-red:#a11a10;
  --deep-blue:#0d4d7a;
  --bright-blue:#0aa3ee;
  --mid-blue:#0b8fd9;
  --red:#d0200a;
  --dark-red:#a8190a;
  --charcoal:#3a3a3a;
  --black:#1a1a1a;
  --grey-band:#efefef;
  --box-grey:#e8e8e8;
  --text:#555;
  --footer:#0f4566;
  --footer-dark:#08304c;
  --banner-red:#961808;
}
*{box-sizing:border-box;margin:0;padding:0}
html,body{width:1200px;height:2190px;overflow:hidden;background:#fff;font-family:"Open Sans",sans-serif;color:var(--text)}
.page{position:relative;width:1200px;height:2190px}
.abs{position:absolute}

.topbar{left:0;top:0;width:1200px;height:41px;background:var(--topbar)}
.topbar-link{top:12px;font-size:13px;color:#fff;display:flex;align-items:center;gap:6px}
.search{left:823px;top:7px;width:202px;height:27px;background:#fff;font-size:12px;color:#aaa;padding:6px 9px}
.search svg{position:absolute;right:6px;top:4px}
.social-sq{top:10px;width:21px;height:21px;border-radius:3px;background:#3aa0e6}

.header{left:0;top:41px;width:1200px;height:108px;background:#fff}
.logo{left:46px;top:64px;display:flex;align-items:center;gap:10px;font-weight:700;font-size:22px;color:var(--brand-red)}
.logo-mark{width:40px;height:40px;border-radius:50%;background:var(--nav-blue)}
.nav{left:403px;top:84px;display:flex;gap:21px;font-size:13.5px;font-weight:600;color:var(--nav-blue)}
.nav .active{color:var(--brand-red);position:relative}
.nav .active::before{content:"";position:absolute;left:-4px;right:-4px;top:-9px;height:3px;background:var(--brand-red)}
.dropdown{left:802px;top:120px;width:221px}
.dropdown div{height:33px;line-height:33px;padding-left:11px;font-size:12.5px;color:#fff;background:#4a4a4a;border-bottom:1px solid #5c5c5c}
.dropdown .current{background:var(--brand-red)}

.hero{left:0;top:149px;width:1200px;height:455px;background:linear-gradient(180deg,#2a2a3c 0%,#9a4a4a 28%,#e8603a 38%,#4a3a48 50%,#141826 70%,#0c0f18 100%)}

.title{left:46px;top:630px;font-family:"Anton",sans-serif;font-size:36px;color:#111;letter-spacing:.5px}
.title-rule{left:46px;top:682px;width:82px;height:6px;background:var(--nav-blue)}
.crumb{left:46px;top:705px;font-size:14px;font-weight:600;color:#333}
.share{left:46px;top:740px;font-size:14px;color:var(--red)}
.intro{left:46px;top:779px;width:740px;font-size:14px;line-height:19px;color:#666}
.intro p{margin-bottom:8px}

.band{left:0;top:910px;width:1200px;height:407px;background:var(--grey-band)}
.card{color:#fff;text-align:center}
.card-head{display:flex;align-items:center;justify-content:center;font-family:"Anton",sans-serif;font-size:21px;line-height:24px;letter-spacing:.3px}
.card-body{display:flex;align-items:center;justify-content:center;padding:0 30px;font-size:14px;line-height:20px}
.card-price{display:flex;align-items:center;justify-content:center;font-size:28px;font-weight:700}
.strategic{left:46px;top:981px;width:264px}
.strategic .card-head{height:68px;background:var(--deep-blue)}
.strategic .card-body{height:135px;background:#0a4470}
.strategic .card-price{height:58px;background:#083a60}
.programs{left:310px;top:953px;width:318px}
.programs .card-head{height:86px;background:var(--bright-blue)}
.programs .card-body{height:161px;background:var(--mid-blue)}
.programs .card-price{height:70px;background:#0a86cf;border-top:1px solid #2b9ee0}
.advert{left:628px;top:981px;width:264px}
.advert .card-head{height:68px;background:var(--red)}
.advert .card-body{height:135px;background:#b01c0a}
.advert .card-price{height:58px;background:var(--dark-red)}
.custom{left:892px;top:981px;width:263px}
.custom .card-head{height:68px;background:var(--charcoal)}
.custom .card-body{height:135px;background:var(--black)}
.custom .card-price{height:58px;background:#161616}

.action{left:46px;width:450px;height:48px;background:var(--box-grey);border:1px solid #d2d2d2;padding-left:11px;line-height:46px;font-size:16px;font-weight:600}

.banner{left:46px;top:1600px;width:1109px;height:53px;border-radius:10px;background:var(--banner-red);color:#fff;font-size:17px;font-weight:600;line-height:53px;padding-left:14px}
.tier{font-size:25px;font-weight:600;color:#222}
.sponsor-box{height:78px;background:#f4f4f4;border:1px solid #bdbdbd;display:flex;align-items:center;justify-content:space-around;font-size:24px;font-weight:700}
.sponsor-box span{color:#1b3f7a}

.footer{left:0;top:1876px;width:1200px;height:270px;background:linear-gradient(180deg,#0f4566,#0c3b5a)}
.f-head{font-size:22px;font-weight:600;color:#fff}
.f-list{list-style:disc;color:#fff;font-size:15px;line-height:26px;padding-left:18px}
.f-contact{font-size:15px;color:#fff;line-height:32px}
.f-contact div{display:flex;align-items:center;gap:12px}
.badge{left:646px;top:1916px;width:255px;height:180px;background:#fff;border:2px solid #2f69a8}
.badge-inner{position:absolute;left:20px;top:40px;width:211px;height:90px;background:#2f69a8}
.f-social{top:1963px;width:27px;height:27px;border-radius:50%;background:#b8c2cc}
.bottombar{left:0;top:2146px;width:1200px;height:44px;background:var(--footer-dark);color:#fff;font-size:12.5px;text-align:center;line-height:44px}
</style>
</head>
<body>
<div class="page">

  <div class="abs topbar"></div>
  <div class="abs topbar-link" style="left:468px">
    <svg width="11" height="12" viewBox="0 0 12 12"><path d="M3 1l2 3-1 1c1 2 2 3 4 4l1-1 3 2-1 2C6 12 0 6 1 2z" fill="#fff"/></svg>CONTACT US</div>
  <div class="abs topbar-link" style="left:592px">
    <svg width="11" height="12" viewBox="0 0 12 12"><circle cx="6" cy="3.5" r="3" fill="#fff"/><path d="M0 12c0-4 3-5 6-5s6 1 6 5z" fill="#fff"/></svg>SIGN IN</div>
  <div class="abs topbar-link" style="left:688px">
    <svg width="18" height="12" viewBox="0 0 18 12"><path d="M1 5l5-4 3 2 3-2 5 4-8 6z" fill="#fff"/></svg>JOIN/RENEW</div>
  <div class="abs search">Search
    <svg width="20" height="20" viewBox="0 0 20 20"><circle cx="8" cy="8" r="6" stroke="#111" stroke-width="2.4" fill="none"/><path d="M12.5 12.5l6 6" stroke="#111" stroke-width="2.6"/></svg></div>
  <div class="abs social-sq" style="left:1032px"></div>
  <div class="abs social-sq" style="left:1057px;background:#3b5fa8"></div>
  <div class="abs social-sq" style="left:1082px"></div>
  <div class="abs social-sq" style="left:1107px;background:#4b86c7"></div>
  <div class="abs social-sq" style="left:1132px;background:#d42a1a"></div>

  <div class="abs header"></div>
  <div class="abs logo"><span class="logo-mark"></span>Metro Talent Guild</div>
  <nav class="abs nav">
    <span>OUR NEW WEBSITE</span><span>ABOUT US</span><span>MEMBERSHIP</span><span>EVENTS</span>
    <span class="active">SPONSORSHIPS</span><span>CAREER CENTER</span><span>HR RESOURCES</span>
  </nav>

  <div class="abs hero" role="img" aria-label="City skyline at dusk with a lit skyscraper against an orange sunset sky"></div>

  <div class="abs dropdown">
    <div class="current">SPONSORSHIP OPPORTUNITIES</div>
    <div>STRATEGIC PARTNERSHIP</div>
    <div>PROGRAMS / EVENTS</div>
    <div>ADVERTISING / PROMOTION</div>
  </div>

  <h1 class="abs title">INVITATION FOR SPONSORS</h1>
  <div class="abs title-rule"></div>
  <div class="abs crumb">Sponsorships » Sponsorship Opportunities</div>
  <div class="abs share">Share |</div>
  <div class="abs intro">
    <p>Thank you for your interest in Metro Talent Guild.</p>
    <p>As a premier Talent Society chapter, we offer many opportunities to increase your exposure to the New York City HR community.</p>
    <p>Choose the sponsorship category that best meets your needs:</p>
  </div>

  <div class="abs band"></div>
  <div class="abs card strategic">
    <div class="card-head">STRATEGIC &nbsp;&nbsp;&nbsp;/<br>PARTNERSHIP</div>
    <div class="card-body">Opportunities for a strategic sponsorship at different levels, each providing a valuable set of great benefits</div>
    <div class="card-price">$3,500+</div>
  </div>
  <div class="abs card programs">
    <div class="card-head">PROGRAMS &nbsp;&nbsp;/<br>EVENTS</div>
    <div class="card-body">Opportunities for a strategic sponsorship at different levels, each providing a valuable set of great benefits</div>
    <div class="card-price">$500+</div>
  </div>
  <div class="abs card advert">
    <div class="card-head">ADVERTISING &nbsp;/<br>PROMOTION</div>
    <div class="card-body">Opportunities for a strategic sponsorship at different levels, each providing a valuable set of great benefits</div>
    <div class="card-price">$150+</div>
  </div>
  <div class="abs card custom">
    <div class="card-head">CUSTOM &nbsp;&nbsp;/</div>
    <div class="card-body">Build your own sponsorship program from our variety of opportunities</div>
    <div class="card-price">$250+</div>
  </div>

  <div class="abs action" style="top:1392px;color:var(--nav-blue)">More about our sponsorship packages</div>
  <div class="abs action" style="top:1448px;color:var(--brand-red)">Book your sponsorship package</div>
  <div class="abs action" style="top:1504px;color:#222">Contact our sponsorship team</div>

  <div class="abs banner">Thank You to Our Corporate Sponsors</div>
  <div class="abs tier" style="left:58px;top:1694px">Gold</div>
  <div class="abs tier" style="left:624px;top:1694px">Silver</div>
  <div class="abs sponsor-box" style="left:46px;top:1744px;width:523px"><span>Harlow Marsh</span><span>Transit Perks Co</span></div>
  <div class="abs sponsor-box" style="left:617px;top:1746px;width:523px"><span>Staffwell</span><span>Beacon Benefits Group</span></div>

  <div class="abs footer"></div>
  <div class="abs f-head" style="left:52px;top:1908px">Navigation</div>
  <ul class="abs f-list" style="left:52px;top:1958px">
    <li>About Us</li><li>Membership</li><li>Events</li><li>Career Center</li><li>Sponsorships</li><li>HR Resources</li>
  </ul>
  <div class="abs f-head" style="left:294px;top:1910px">Contact us</div>
  <div class="abs f-contact" style="left:300px;top:1954px">
    <div><svg width="16" height="16" viewBox="0 0 12 12"><path d="M3 1l2 3-1 1c1 2 2 3 4 4l1-1 3 2-1 2C6 12 0 6 1 2z" fill="#fff"/></svg>Phone: 800-555-0147</div>
    <div><svg width="16" height="16" viewBox="0 0 16 16"><rect x="4" y="1" width="8" height="4" fill="none" stroke="#fff" stroke-width="1.5"/><rect x="1" y="5" width="14" height="7" fill="#fff"/><rect x="4" y="10" width="8" height="5" fill="#0f4566" stroke="#fff" stroke-width="1.5"/></svg>Fax: 800-555-0198</div>
    <div><svg width="16" height="12" viewBox="0 0 16 12"><rect x="0" y="0" width="16" height="12" fill="#fff"/><path d="M0 0l8 7 8-7" stroke="#0f4566" stroke-width="1.5" fill="none"/></svg>Email: info@metrotalentguild.example</div>
  </div>
  <div class="abs badge"><div class="badge-inner"></div></div>
  <div class="abs f-head" style="left:968px;top:1904px">Connect With Us</div>
  <div class="abs f-social" style="left:974px"></div>
  <div class="abs f-social" style="left:1005px"></div>
  <div class="abs f-social" style="left:1036px"></div>
  <div class="abs f-social" style="left:1067px"></div>
  <div class="abs f-social" style="left:1098px"></div>
  <div class="abs bottombar">©2016 Metro Talent Guild ALL RIGHT RESERVED</div>
</div>
</body>
</html>
```